Velvet Riddles funky jazz CD Layout design

Cd cover for smooth jazz / funky groove piano based artist. Winning cover designer should be prepared to complete 6 panel CD package layout.

Brent Holloway Velvet Riddles

Melodic, organic, soulful, elegant, romantic and fun uptempo instrumental soul / jazz music. Cd design should translate well to 12" sq. flats for promotional use. Looking for a clean, sophisticated, design with artist's name and title prominent.
check out www.hollowaytunes.example for musical and graphic samples of what I do. Thanks, brent

Target Market(s)

Smooth Jazz and Instrumental music fans. Wine lovers, the good life.

Industry/Entity Type

Promotional

Font styles to use
Sans Serif

Requirements
Must have
• Elements delivered also as separate files for full package layout and flyer usage.
Nice to have
• UPDATE: See FILES:

My team likes this concept, with the eyes........ and I'd like to get submissions using some of these pics, with alternate, classy TYPE. Current preference is w/ lace fan #....675, but we're open. No Burka look though.

Winner will also be expected to layout 6 panel design. Thanks, Brent

Possible elements: Piano or implied shape or shadow. Sultry woman, possibly close up of enigmatic ( secret) expression.
Has to be compelling design, don't put a piano keyboard just for the sake of it.
Strong Ravelle-like graphic retro / or Silver Lantern Records block style.
Should not have
• No Burka look Flowery, fantasy or hand drawn illustration style.

```html
<!DOCTYPE html>
<html lang="en">
<head>
<meta charset="utf-8">
<title>Brent Holloway – Velvet Riddles</title>
<link rel="stylesheet" href="https://fonts.googleapis.com/css2?family=Great+Vibes&family=Cormorant+Garamond:wght@500&family=Open+Sans:wght@400&display=swap">
<style>
  :root {
    --page-top: #f3f2f0;
    --page-bottom: #e6e3df;
    --ink-red: #b5242c;
    --disc-dark: #232022;
    --disc-brown: #6a4a44;
    --disc-grey: #8c8584;
    --disc-orange: #e4472c;
    --disc-red: #c8202a;
    --disc-light: #f4f1f0;
    --disc-rim: #dcdcdc;
    --flap: #2f2a2d;
    --flap-edge: #1e1a1c;
    --sleeve: #ffffff;
    --white: #ffffff;
    --body-text: #4a4a4a;
  }
  html, body {
    margin: 0;
    padding: 0;
    overflow: hidden;
  }
  body {
    width: 960px;
    height: 1200px;
  }
  .canvas {
    position: relative;
    width: 960px;
    height: 1200px;
    overflow: hidden;
    background: linear-gradient(180deg, var(--page-top), var(--page-bottom));
  }
  .sleeve-flap {
    position: absolute;
    left: 200px;
    top: 490px;
    width: 570px;
    height: 104px;
    background: linear-gradient(180deg, #3a3438, var(--flap));
    border-radius: 10px 10px 0 0;
    border-bottom: 6px solid var(--flap-edge);
  }
  .disc {
    position: absolute;
    left: 200px;
    top: 17px;
    width: 568px;
    height: 568px;
  }
  .disc-name {
    font-family: "Great Vibes", cursive;
    font-size: 31px;
    fill: var(--white);
  }
  .disc-title {
    font-family: "Great Vibes", cursive;
    font-size: 62px;
    fill: var(--white);
  }
  .disc-tagline {
    font-family: "Cormorant Garamond", serif;
    font-weight: 500;
    font-size: 10.5px;
    letter-spacing: 0.2px;
    fill: var(--white);
  }
  .sleeve {
    position: absolute;
    left: 192px;
    top: 592px;
    width: 583px;
    height: 578px;
    background: var(--sleeve);
    box-shadow: 0 2px 4px rgba(0, 0, 0, 0.18);
  }
  .sleeve-titles {
    position: absolute;
    left: 0;
    right: 0;
    top: 166px;
    margin: 0;
    text-align: center;
    color: var(--ink-red);
    font-family: "Great Vibes", cursive;
    font-weight: 400;
    line-height: 1;
  }
  .artist-name {
    display: block;
    font-size: 44px;
    margin-left: 20px;
  }
  .album-title {
    display: block;
    font-size: 90px;
    margin-top: -2px;
  }
  .sleeve-note {
    position: absolute;
    left: 37px;
    right: 40px;
    bottom: 30px;
    margin: 0;
    font-family: "Open Sans", sans-serif;
    font-size: 10.5px;
    line-height: 1.5;
    color: var(--body-text);
  }
</style>
</head>
<body>
<div class="canvas">
  <div class="sleeve-flap"></div>

  <svg class="disc" viewBox="0 0 568 568" xmlns="http://www.w3.org/2000/svg">
    <defs>
      <linearGradient id="disc-base" x1="0" y1="0" x2="1" y2="1">
        <stop offset="0" stop-color="var(--disc-dark)"/>
        <stop offset="0.4" stop-color="#3a3334"/>
        <stop offset="0.75" stop-color="var(--disc-brown)"/>
        <stop offset="1" stop-color="var(--disc-dark)"/>
      </linearGradient>
      <radialGradient id="glow-grey" cx="0.42" cy="0.35" r="0.3">
        <stop offset="0" stop-color="var(--disc-grey)" stop-opacity="0.75"/>
        <stop offset="1" stop-color="var(--disc-grey)" stop-opacity="0"/>
      </radialGradient>
      <radialGradient id="glow-orange" cx="0.3" cy="0.85" r="0.35">
        <stop offset="0" stop-color="var(--disc-orange)" stop-opacity="0.95"/>
        <stop offset="1" stop-color="var(--disc-orange)" stop-opacity="0"/>
      </radialGradient>
      <radialGradient id="glow-red" cx="0.85" cy="0.75" r="0.3">
        <stop offset="0" stop-color="var(--disc-red)"/>
        <stop offset="1" stop-color="var(--disc-red)" stop-opacity="0"/>
      </radialGradient>
      <linearGradient id="glow-light" x1="0" y1="1" x2="1" y2="0">
        <stop offset="0" stop-color="var(--disc-light)" stop-opacity="0.9"/>
        <stop offset="1" stop-color="var(--disc-light)" stop-opacity="0.6"/>
      </linearGradient>
      <clipPath id="disc-shape">
        <circle cx="284" cy="284" r="282"/>
      </clipPath>
    </defs>
    <circle cx="284" cy="284" r="284" fill="var(--disc-rim)"/>
    <g clip-path="url(#disc-shape)" role="img"
       aria-label="Illustration of dancing women in silhouette, a curling piano keyboard, flowing red lines and music notes">
      <rect width="568" height="568" fill="url(#disc-base)"/>
      <rect width="568" height="568" fill="url(#glow-grey)"/>
      <rect width="568" height="568" fill="url(#glow-orange)"/>
      <rect width="568" height="568" fill="url(#glow-red)"/>
      <path d="M150 560 C260 480 300 380 320 300 C400 250 470 240 540 240 L568 240 L568 420 C520 440 470 470 420 500 C360 530 300 560 260 580 Z"
            fill="url(#glow-light)"/>
      <g fill="none" stroke="var(--white)" stroke-opacity="0.55" stroke-width="1">
        <path d="M210 230 C260 300 250 400 170 500"/>
        <path d="M225 225 C280 300 270 410 190 510"/>
        <path d="M240 220 C300 300 290 420 210 520"/>
        <path d="M60 480 C200 470 330 420 420 330 C480 270 530 230 560 200"/>
      </g>
    </g>
    <text class="disc-name" x="293" y="110" text-anchor="middle">Brent Holloway</text>
    <text class="disc-title" x="280" y="165" text-anchor="middle">Velvet Riddles</text>
    <text class="disc-tagline" text-anchor="middle">
      <tspan x="500" y="304">MELODIC, ORGANIC-</tspan>
      <tspan x="500" y="317">SOULFUL, ELEGANT,</tspan>
      <tspan x="500" y="330">ROMANTIC AND</tspan>
      <tspan x="500" y="343">FUN UPTEMPO</tspan>
      <tspan x="500" y="356">INSTRUMENTAL</tspan>
      <tspan x="500" y="369">SOUL</tspan>
      <tspan x="500" y="382">JAZZ MUSIC.</tspan>
    </text>
    <circle cx="284" cy="284" r="40" fill="var(--white)"/>
  </svg>

  <div class="sleeve">
    <h1 class="sleeve-titles">
      <span class="artist-name">Brent Holloway</span>
      <span class="album-title">Velvet Riddles</span>
    </h1>
    <p class="sleeve-note">Lorem ipsum dolor sit amet, consectetur adipiscing elit. Donec orci purus, luctus vitae dignissim eu, iaculis sed purus. Vivamus faucibus, ipsum nec aliquet viverra, leo mauris condimentum.</p>
  </div>
</div>
</body>
</html>
```